website conversion to Wordpress with an updated look and feel

Bright Torque Hub Limited is a company and an online presence, which promotes and sells a branded fuel additive product named “Valmix”.

The existing website is at www.brighttorquehub.co.uk

The site consists of static but attractive pages, a contact form, and most importantly a shopping page which is driven externally using shopvarn.com. Therefore e-commerce coding is NOT required as this task is performed by shopvarn via a plugin.

The website is 4 years old and we intend to revamp the graphics and the image of the company and the website to give it a modern “Windows 10” look!

Less text and less cluttering, Cleaner and easier navigations, bigger and clearer fonts. Simple message to put across to visitors/potential customers. Be creative.

The site needs to be simplified - the detail can/should still be there... But it can be placed deeper down or hidden by the use of dropdowns, callouts, etc.

A couple of good example styles we like are

https://www.brolavent.com/
http://www.4plumtoaster.com/en/#/welcome
https://www.tivoramp.com/

Some specific areas of attention.

homepage - This needs to really reflect the new look-and feel of the website. In addition the product we sell can be used in a number of applications - currently navigation to these different applications is through the moving banner. This needs to be changed. The major areas for access should be

Heating Oil
Vehicles
Marine
Generators

Technical requirements what we want:-
Wordpress (self hosted ) - currently Joomla based
Use of webfonts to improve typographic appearances
Shopvarn integration using plugin
Facebook/Twitter integration
Responsive design (Mobile friendly)
Search Engine friendly and some SEO optimisation
Northwind Analytics / Bing webmaster tracking

Target Market(s)

Owners of Olm branded range cookers and similar - our product fixes a fuel problem specific to these devices.

Also bulk fuel users looking to save money on their fuel costs - product improves fuel efficiency and reduces maintenance.

Industry/Entity Type

E-Commerce

Font styles to use
Sans Serif

Requirements
Must have
• Wordpress design
• Responsive design
• Simple "clean" look and feel
• Use of stock graphics
• a review of all current pages
Nice to have
• Social media integration - blog
• A forum to discuss the product and problems people experience with fuel

```html
<!DOCTYPE html>
<html lang="en">
<head>
<meta charset="utf-8">
<title>Bright Torque Hub — Fuel Additive Specialists</title>
<link href="https://fonts.googleapis.com/css2?family=Anton&family=Open+Sans:wght@300;400;600;700&display=swap" rel="stylesheet">
<style>
:root{
  --green:#7bb043;
  --green-dark:#5f9130;
  --red:#d8262c;
  --ink:#2b2b2b;
  --muted:#6b6b6b;
  --grey-bg:#e6e6e6;
  --grey-box:#8a8a8a;
  --field:#e9e9e9;
  --cream:#eef1e2;
  --black:#0d0d0d;
  --white:#ffffff;
}
*{box-sizing:border-box;margin:0;padding:0}
html,body{width:1200px;height:3295px;overflow:hidden}
body{font-family:"Open Sans",Arial,sans-serif;color:var(--ink);background:var(--white);position:relative}
.wrap{width:890px;margin:0 auto;position:relative;height:100%}
section,header,footer{position:relative;width:1200px;overflow:hidden}

/* header */
.site-header{height:118px;border-top:5px solid var(--green);background:var(--white)}
.brand{position:absolute;left:6px;top:22px;display:flex;align-items:center;gap:10px}
.brand-dot{width:34px;height:34px;border-radius:50%;background:var(--green)}
.brand-name{font-size:30px;font-weight:600;color:var(--green);line-height:1}
.brand-tag{position:absolute;left:50px;top:62px;font-size:11px;color:var(--muted);white-space:nowrap}
.main-nav{position:absolute;left:306px;top:42px;display:flex;gap:4px}
.main-nav a{font-size:12.5px;font-weight:700;color:var(--ink);text-decoration:none;padding:9px 9px;text-transform:uppercase}
.main-nav a.current{background:var(--red);color:var(--white)}

/* hero */
.hero{height:459px;background:var(--black)}
.hero-photo{position:absolute;inset:0;background:radial-gradient(ellipse at 75% 55%,#8d8d8d 0%,#3a3a3a 35%,#0a0a0a 70%)}
.hero-title{position:absolute;left:175px;top:120px;font-family:"Anton",Impact,sans-serif;font-size:50px;line-height:1.12;color:var(--white);letter-spacing:.5px}
.btn{display:inline-block;font-size:13px;font-weight:600;color:var(--white);text-transform:uppercase;text-decoration:none;padding:9px 14px}
.btn-green{background:var(--green)}
.btn-red{background:var(--red)}
.hero .btn{position:absolute;left:175px;top:245px;font-size:11px;padding:7px 10px}

/* welcome */
.welcome{height:398px;background:var(--grey-bg);text-align:center}
.welcome h1{padding-top:62px;font-size:48px;font-weight:400;color:#3a3a3a}
.welcome h1 span{color:var(--green)}
.welcome p{width:780px;margin:16px auto 0;font-size:13.5px;line-height:1.5;color:#333}
.welcome .hl{color:var(--red)}
.welcome .btn{margin-top:18px;font-size:12px;padding:8px 24px}

/* feature tiles */
.features{height:417px;background:var(--white)}
.tiles{display:flex;width:890px;margin:0 auto}
.tile{width:297px;height:417px;padding:0 24px;color:var(--white);position:relative}
.tile-green{background:var(--green)}
.tile-grey{background:var(--grey-box)}
.tile-icon{width:108px;height:108px;border-radius:50%;background:var(--white);margin-top:56px;display:flex;align-items:center;justify-content:center}
.video-thumb{width:262px;height:112px;margin:55px 0 0 -6px;background:linear-gradient(135deg,#c9c9c9,#6c6c6c 60%,#b83a3a)}
.tile h3{font-size:31px;font-weight:400;margin-top:40px;white-space:nowrap;letter-spacing:-.5px}
.tile p{font-size:12px;line-height:1.4;margin-top:8px}
.tile .more{position:absolute;left:24px;bottom:48px;font-size:13px;color:var(--white);text-decoration:none}

/* about / blog / testimonials */
.info{height:503px}
.col{position:absolute;top:55px}
.col h2{font-size:40px;font-weight:400;color:#222;letter-spacing:-.5px}
.col-who{left:165px;width:270px}
.col-blog{left:461px;width:280px}
.col-test{left:769px;width:275px}
.col-who p{font-size:13px;line-height:1.5;margin-top:14px;text-align:justify}
.ticks{list-style:none;margin-top:14px}
.ticks li{font-size:12.5px;padding:6px 0;border-bottom:1px solid #ddd;white-space:nowrap;overflow:hidden}
.ticks li:before{content:"«";color:var(--green);font-weight:700;margin-right:14px}
.ticks li:nth-child(even){color:var(--red)}
.more-link{display:inline-block;margin-top:26px;font-size:13px;color:var(--red);text-decoration:none}
.post{display:flex;gap:10px;margin-top:14px}
.post:first-of-type{margin-top:22px}
.post-thumb{width:40px;height:40px;background:linear-gradient(#b9a892,#6e6458);flex:none}
.post h4{font-size:12px;font-weight:400;color:var(--green)}
.post p{font-size:11.5px;color:#333}
.post small{font-size:10px;color:var(--red)}
.col-blog .more-link{color:#333;margin-top:22px}
.quote{margin-top:22px;background:#d9d9d9;padding:16px 18px;font-size:12.5px;line-height:1.5;position:relative}
.quote:after{content:"";position:absolute;left:30px;bottom:-16px;border:8px solid transparent;border-top-color:#d9d9d9;border-left-color:#d9d9d9}
.author{display:flex;align-items:center;gap:12px;margin-top:18px}
.author-photo{width:64px;height:64px;border-radius:50%;background:linear-gradient(#d2c2b2,#4a3d35)}
.author small{font-size:10px;color:#555;display:block}
.author small b{color:var(--green);font-weight:400}
.author strong{font-size:13px;color:var(--green)}

/* working areas */
.areas{height:590px;background:#111}
.areas-photo{position:absolute;inset:0;background:linear-gradient(135deg,#2d2d2d 0%,#0e0e0e 45%,#4d4a44 80%,#1a1a1a 100%)}
.areas h2{position:absolute;top:60px;width:100%;text-align:center;font-size:32px;font-weight:400;color:var(--white)}
.card{position:absolute;width:405px;height:178px;padding:16px 20px}
.card h3{font-size:31px;font-weight:400;letter-spacing:-.5px}
.card p{font-size:12.5px;line-height:1.4;margin-top:4px}
.card a{display:inline-block;margin-top:10px;font-size:13px;text-decoration:none}
.card-green{background:var(--green);color:var(--white)}
.card-green a{color:var(--white)}
.card-light{background:#f2f2f2;color:#333}
.card-light h3{color:var(--green)}
.card-light a{color:#333}

/* inquiry */
.inquiry{height:288px}
.inquiry h2{text-align:center;font-size:34px;font-weight:400;padding-top:50px;letter-spacing:.5px}
.field{position:absolute;width:233px;height:44px;background:var(--field);border:1px solid #d6d6d6;font-size:12px;color:#999;padding:12px 10px}
.field.msg{height:99px}
.form-btn{position:absolute;left:906px;width:132px;height:44px;color:var(--white);font-size:13px;font-weight:600;display:flex;align-items:center;justify-content:center}

/* promo band */
.promo{height:110px;background:var(--cream)}
.promo h2{position:absolute;left:175px;top:26px;font-size:36px;font-weight:400;color:#333}
.promo h2 span{color:var(--red)}
.promo p{position:absolute;left:175px;top:74px;font-size:12px;font-weight:600}
.promo .btn{position:absolute;left:840px;top:32px;width:187px;text-align:center;font-size:22px;font-weight:400;padding:9px 0}

/* footer */
.site-footer{height:412px;background:var(--black);color:var(--white)}
.fcol{position:absolute;top:72px}
.fcol h4{font-size:17px;font-weight:400;margin-bottom:18px;white-space:nowrap}
.fcol ul{list-style:none}
.fcol li{font-size:11.5px;line-height:2.5}
.fcol.apps li{color:var(--red)}
.contact li{display:flex;align-items:center;gap:10px;line-height:1.4;margin-bottom:16px}
.subscribe{display:flex;margin-top:4px}
.subscribe span{width:170px;height:26px;background:#f0f0f0;color:#999;font-size:10px;padding:6px 10px}
.subscribe b{width:84px;height:26px;background:var(--green);font-size:10px;font-weight:600;display:flex;align-items:center;justify-content:center}
.fbrand{position:absolute;left:796px;top:80px;width:230px}
.fbrand-mark{display:flex;align-items:center;gap:10px}
.fbrand-mark i{width:44px;height:44px;border-radius:50%;background:#555}
.fbrand-mark span{font-size:30px;font-weight:600;color:#666}
.copyright{font-size:11px;margin-top:20px}
.copyright b{color:var(--green)}
.badge-row{display:flex;gap:10px;margin-top:56px}
.badge{width:92px;height:36px;background:#3d6fb6;flex:none}
.badge-row p{font-size:9.5px;color:#aaa;line-height:1.35}
.fbottom{position:absolute;left:0;top:378px;width:1200px;border-top:1px solid #2a2a2a;height:34px}
.fbottom p{position:absolute;left:165px;top:10px;font-size:10px;color:#aaa}
.social{position:absolute;left:970px;top:8px;display:flex;gap:6px}
.social i{width:18px;height:18px;border-radius:50%;border:1px solid #999}
</style>
</head>
<body>

<header class="site-header">
  <div class="wrap">
    <div class="brand"><i class="brand-dot"></i><span class="brand-name">brighttorquehub</span></div>
    <div class="brand-tag">Economy &amp; Efficiency &amp; Environment</div>
    <nav class="main-nav">
      <a class="current" href="#">Home</a><a href="#">How it works</a><a href="#">Environment</a><a href="#">Applications</a><a href="#">Contact</a><a href="#">Store</a><a href="#">Brighttorquehub Blog</a>
    </nav>
  </div>
</header>

<section class="hero">
  <div class="hero-photo" role="img" aria-label="Dark studio photograph of a white sports car"></div>
  <h1 class="hero-title">The Fule Additive<br>Specialsits</h1>
  <a class="btn btn-green" href="#">Buy Valmix now</a>
</section>

<section class="welcome">
  <h1>Welcome to <span>brighttorquehub</span></h1>
  <p>With the cost of fuel constantly increasing – imagine the benefits to you if you could improve vehicle MPG by even a few percent. Whether you are a multinational road haulier running a fleet of vehicles or if you only drive to the shops once a week <span class="hl">VALMIX</span> can save you money on your fuel bill and reduce the impact to the environment.</p>
  <p><span class="hl">VALMIX</span> is a 100% organic fuel treatment which reduces the harmful effects of impurities in modern fuels and improves combustion. It is a fantastic product with huge benefits for the both the domestic user and for industry.</p>
  <p>Already well-established in shipping (<span class="hl">VALMIX</span> treated 30 million tonnes of fuel last year) it is now available in the UK, offering improved engine efficiency, reduced pollutants and better fuel economy.</p>
  <a class="btn btn-red" href="#">Read more</a>
</section>

<section class="features">
  <div class="tiles">
    <article class="tile tile-green">
      <div class="tile-icon">
        <svg width="56" height="56" viewBox="0 0 56 56"><path d="M28 4 C18 18 12 26 12 36 a16 16 0 0 0 32 0 C44 26 38 18 28 4Z" fill="#7bb043"/><rect x="19" y="32" width="18" height="8" rx="2" fill="#fff"/><circle cx="22" cy="42" r="2.5" fill="#fff"/><circle cx="34" cy="42" r="2.5" fill="#fff"/></svg>
      </div>
      <h3>FUEL SAVING TIPS</h3>
      <p>Greitutous octopus niacodumtimale. Quote mean an estimate et non interruptus sleit um. Sic tempus fugit esperanto hoc.</p>
      <a class="more" href="#">READ MORE &nbsp;›</a>
    </article>
    <article class="tile tile-grey">
      <div class="video-thumb" role="img" aria-label="Video still of a fuel nozzle filling a car"></div>
      <h3>WATCH OUR VIDEO</h3>
      <p>Greitutous octopus niacodumtimale. Quote mean an estimi@gnate et non inter cllruptus sle itum. Sic tempus fugit esper.</p>
      <a class="more" href="#">READ MORE &nbsp;›</a>
    </article>
    <article class="tile tile-green">
      <div class="tile-icon">
        <svg width="56" height="56" viewBox="0 0 56 56"><path d="M28 4 C18 18 12 26 12 36 a16 16 0 0 0 32 0 C44 26 38 18 28 4Z" fill="#7bb043"/><path d="M28 28 L22 46 M28 28 L34 46 M24 40 H32" stroke="#fff" stroke-width="2.5" fill="none"/><circle cx="28" cy="26" r="3" fill="#fff"/></svg>
      </div>
      <h3>EMISSIONS</h3>
      <p>Greitutous octopus niacodumtimale. Quote mean an estimate et non interru ctlptus sleit um. Sic tempus fugit esperanto hoc.</p>
      <a class="more" href="#">READ MORE &nbsp;›</a>
    </article>
  </div>
</section>

<section class="info">
  <div class="col col-who">
    <h2>Who are we?</h2>
    <p>Lorem ipsum dolor sit amet conse ctetur adipiscing elit, sed do eiusmod tempor incididunt ut labore et dolore magna aliqua. Ut enim ad minim veniam, quis nostrud exercitation ullamco laboris nisi ut aliquip ex ea commodo. Duis aute irure dolor in reprehenderit in voluptate velit esse.</p>
    <ul class="ticks">
      <li>LOREM IPSUM DOLOR SIT CONSE</li>
      <li>SED UT PERSPICIATIS OMNIS ISTE</li>
      <li>LOREM IPSUM DOLOR SIT CONSE</li>
      <li>SED UT PERSPICIATIS OMNIS ISTE</li>
    </ul>
    <a class="more-link" href="#">READ MORE &nbsp;›</a>
  </div>
  <div class="col col-blog">
    <h2>Blog</h2>
    <div class="post"><div class="post-thumb" role="img" aria-label="Author thumbnail"></div><div><h4>Eadipscing elit, sed dhgin dfiho</h4><p>Tempor incitifidid ut laboofgin rervdfdif</p><small>Posted on 6 March, 2015</small></div></div>
    <div class="post"><div class="post-thumb" role="img" aria-label="Author thumbnail"></div><div><h4>Eadipscing elit, sed dhgin dfiho</h4><p>Tempor incitifidid ut laboofgin rervdfdif</p><small>Posted on 6 March, 2015</small></div></div>
    <div class="post"><div class="post-thumb" role="img" aria-label="Author thumbnail"></div><div><h4>Eadipscing elit, sed dhgin dfiho</h4><p>Tempor incitifidid ut laboofgin rervdfdif</p><small>Posted on 6 March, 2015</small></div></div>
    <div class="post"><div class="post-thumb" role="img" aria-label="Author thumbnail"></div><div><h4>Eadipscing elit, sed dhgin dfiho</h4><p>Tempor incitifidid ut laboofgin rervdfdif</p><small>Posted on 6 March, 2015</small></div></div>
    <a class="more-link" href="#">VIEW MORE &nbsp;›</a>
  </div>
  <div class="col col-test">
    <h2>Testimonials</h2>
    <div class="quote">Lorem ipsum dolor sit amet conse ctetur adipiscing elit, sed do eiusmod tempor incididunt ut labore et dolore magna aliqua. Lorem ipsum dolor sit amet conse ctetur adipiscing elit, sed do eiusmod tempor incididunt ut labore et dolore magna aliqua.</div>
    <div class="author"><div class="author-photo" role="img" aria-label="Customer portrait"></div><div><small>Programmer, <b>Northwind</b></small><strong>MAYA RENTOL</strong></div></div>
    <a class="more-link" href="#">VIEW MORE &nbsp;›</a>
  </div>
</section>

<section class="areas">
  <div class="areas-photo" role="img" aria-label="Close-up photograph of an engine bay"></div>
  <h2>OUR SPECIALIZED WORKING AREA</h2>
  <article class="card card-green" style="left:184px;top:137px"><h3>HEATING OIL</h3><p>Aenean nonummy hendrerit mau phasellres acfsjc etur ridic ulusm dui fusce feu. Cras vitae neque turpis, pharetra ante elit,...</p><a href="#">READ MORE &nbsp;›</a></article>
  <article class="card card-light" style="left:610px;top:137px"><h3>VELICLES</h3><p>Aenean nonummy hendrerit mau phasellres acfsjc etur ridic ulusm dui fusce feu. Cras vitae neque turpis, pharetra ante elit,...</p><a href="#">READ MORE &nbsp;›</a></article>
  <article class="card card-light" style="left:184px;top:335px"><h3>MARINE</h3><p>Aenean nonummy hendrerit mau phasellres acfsjc etur ridic ulusm dui fusce feu. Cras vitae neque turpis, pharetra ante elit,...</p><a href="#">READ MORE &nbsp;›</a></article>
  <article class="card card-green" style="left:610px;top:335px"><h3>GENERATORS</h3><p>Aenean nonummy hendrerit mau phasellres acfsjc etur ridic ulusm dui fusce feu. Cras vitae neque turpis, pharetra ante elit,...</p><a href="#">READ MORE &nbsp;›</a></article>
</section>

<section class="inquiry">
  <h2>QUICK INQUIRY</h2>
  <div class="field" style="left:165px;top:124px">Name</div>
  <div class="field" style="left:412px;top:124px">Phone</div>
  <div class="field msg" style="left:659px;top:124px">Message</div>
  <div class="field" style="left:165px;top:179px">E-mail</div>
  <div class="field" style="left:412px;top:179px">Company</div>
  <div class="form-btn" style="top:124px;background:var(--green)">RESET</div>
  <div class="form-btn" style="top:179px;background:var(--red)">SUBMIT</div>
</section>

<section class="promo">
  <h2><span>VALMIX</span> has advantages for engines</h2>
  <p>LOREM IPSUM DOLOR SIT AMET, CONSECTETUR ADIPIS CINOFGD DFOGD SFOGRID EXERCITATION !</p>
  <a class="btn btn-green" href="#">BUY NOW</a>
</section>

<footer class="site-footer">
  <div class="fcol" style="left:165px"><h4>QUICK LINKS</h4>
    <ul><li>Home</li><li>How It Works</li><li>Environment</li><li>Applications</li><li>Contact</li><li>Store</li><li>Brighttorquehub Blog</li></ul>
  </div>
  <div class="fcol apps" style="left:313px"><h4>APPLICATIONS</h4>
    <ul><li>Transport</li><li>Heating oil</li><li>Olm and Oil</li><li>Industry and fuel burners</li><li>Fuel saving tips</li><li>Marine and yachting</li><li>Medium</li></ul>
  </div>
  <div class="fcol contact" style="left:489px"><h4>CONTACT INFO</h4>
    <ul>
      <li><svg width="12" height="16" viewBox="0 0 12 16"><path d="M6 0a6 6 0 0 0-6 6c0 4 6 10 6 10s6-6 6-10a6 6 0 0 0-6-6z" fill="#ccc"/><circle cx="6" cy="6" r="2" fill="#0d0d0d"/></svg><span style="font-size:10.5px">7 Fenwick Yard, Marrow Lane, Oldbury,<br>Westshire, WS9 2QT</span></li>
      <li><svg width="14" height="14" viewBox="0 0 14 14"><path d="M3 1l3 3-2 2a8 8 0 0 0 4 4l2-2 3 3-2 2C5 13 1 9 1 3z" fill="#ccc"/></svg><span style="font-size:10.5px">0800 214 3390</span></li>
      <li><svg width="14" height="14" viewBox="0 0 14 14"><rect x="1" y="3" width="12" height="8" fill="#ccc"/></svg><span style="font-size:10.5px">555-018-2244</span></li>
      <li><svg width="14" height="14" viewBox="0 0 14 14"><rect x="1" y="3" width="12" height="8" fill="none" stroke="#ccc"/><path d="M1 3l6 5 6-5" stroke="#ccc" fill="none"/></svg><span style="font-size:10.5px">support@brighttorquehub.com</span></li>
    </ul>
    <div class="subscribe"><span>Your E-mail address</span><b>SUBSCRIBE</b></div>
  </div>
  <div class="fbrand">
    <div class="fbrand-mark"><i></i><span>VALMIX</span></div>
    <p class="copyright">© 2015 <b>BrightTorqueHub</b>. All rights reserved.</p>
    <div class="badge-row"><div class="badge"></div><p>At vero eos et accusamus et iusto odio dignissimos. Lorem ipsum dolor sit amet, consectetur adipisi sed do eiusm tempor incididunt.</p></div>
  </div>
  <div class="fbottom">
    <p>All Rights Reserved. 2015. Brighttorquehub.</p>
    <div class="social"><i></i><i></i><i></i></div>
  </div>
</footer>

</body>
</html>
```